Booth flyer

I am looking for a flyer to pass out either at a booth that is set up at an event or to place as a flyer on a car. Quikko Tza is an affordable light reaction training device that will fit everyone's budget and flexible enough for any imaginable use. Our website is Quikkotza.online and Instagram is Quikko.Tza

```html
<!DOCTYPE html>
<html lang="en">
<head>
<meta charset="utf-8">
<title>Quikko Tza – Reaction Light Training</title>
<link rel="stylesheet" href="https://fonts.googleapis.com/css2?family=Rajdhani:wght@400;500;600;700&display=swap">
<style>
  :root {
    --red: #e83744;
    --red-icon: #e8414b;
    --pink: #f7c4cb;
    --charcoal: #333336;
    --ink: #2b2b2e;
    --white: #ffffff;
    --photo-dark: #1b1a2a;
    --photo-mid: #3a3552;
  }
  * { box-sizing: border-box; margin: 0; padding: 0; }
  html, body { width: 846px; height: 1200px; overflow: hidden; background: var(--white); }
  body { font-family: "Rajdhani", sans-serif; color: var(--ink); position: relative; }

  .brand {
    position: absolute; left: 48px; top: 42px;
    font-size: 46px; font-weight: 700; color: var(--ink); letter-spacing: 0.5px;
    display: flex; align-items: center; gap: 12px;
  }
  .brand-dot { width: 18px; height: 18px; border-radius: 50%; background: var(--red); }

  .tagline { position: absolute; right: 46px; top: 38px; text-align: right; line-height: 1; }
  .tagline-title { font-size: 30px; font-weight: 600; letter-spacing: 1px; color: var(--ink); }
  .tagline-url { font-size: 24px; font-weight: 400; letter-spacing: 1px; color: var(--ink); margin-top: 2px; }

  .hero { position: absolute; left: 0; top: 130px; width: 423px; height: 470px; background: var(--red); padding: 76px 0 0 48px; }
  .hero-headline { color: var(--white); font-size: 56px; font-weight: 700; line-height: 45px; letter-spacing: 1px; }
  .hero-sub { color: var(--pink); font-size: 26px; font-weight: 700; line-height: 25px; margin-top: 30px; letter-spacing: 0.5px; }
  .hero-note { color: var(--white); font-size: 20px; font-weight: 600; line-height: 21px; margin-top: 20px; letter-spacing: 0.5px; }

  .details { position: absolute; left: 0; top: 600px; width: 423px; height: 470px; background: var(--charcoal); padding: 76px 0 0 47px; color: var(--white); }
  .details-title { font-size: 24px; font-weight: 700; line-height: 24px; letter-spacing: 0.5px; }
  .details-body { font-size: 18px; font-weight: 500; line-height: 21.7px; margin-top: 12px; width: 350px; }
  .details-body strong { font-weight: 700; }
  .benefits-title { font-size: 24px; font-weight: 700; margin-top: 52px; letter-spacing: 0.5px; }
  .benefits { display: flex; margin-top: 12px; }
  .benefit { border-left: 3px solid var(--white); padding-left: 6px; font-size: 17px; font-weight: 700; line-height: 15.5px; color: #d6d6da; letter-spacing: 0.3px; }
  .benefit:nth-child(1) { width: 137px; }
  .benefit:nth-child(2) { width: 101px; }

  .photo {
    position: absolute; left: 423px; top: 130px; width: 423px; height: 940px;
    background:
      radial-gradient(ellipse at 60% 40%, rgba(201,46,58,0.75), transparent 55%),
      linear-gradient(180deg, var(--photo-dark) 0%, var(--photo-mid) 55%, var(--photo-dark) 100%);
  }

  .contact { position: absolute; left: 0; top: 1120px; width: 846px; height: 36px; }
  .contact-item { position: absolute; top: 6px; display: flex; align-items: center; gap: 10px; font-size: 20px; font-weight: 500; color: var(--ink); }
  .contact-item svg { width: 22px; height: 24px; }
  .contact-rule { position: absolute; top: 12px; width: 1px; height: 12px; background: #cfcfcf; }
</style>
</head>
<body>
  <header>
    <div class="brand"><span class="brand-dot"></span>Quikko Tza</div>
    <div class="tagline">
      <div class="tagline-title">REACTION LIGHT TRAINING</div>
      <div class="tagline-url">WWW.QUIKKOTZA.ONLINE</div>
    </div>
  </header>

  <section class="hero">
    <h1 class="hero-headline">BRING YOUR<br>TRAINING<br>TO THE NEXT<br>LEVEL</h1>
    <p class="hero-sub">AFFORDABLE LIGHT REACTION<br>TRAINING DEVICE</p>
    <p class="hero-note">FLEXIBLE ENOUGH FOR ANY<br>IMAGINABLE USE</p>
  </section>

  <section class="details">
    <h2 class="details-title">UP YOUR GAME WITH<br>REACTION TRAINING LIGHTS</h2>
    <p class="details-body">An easy to use, multi-light training system <strong>perfect for improving your visual processing</strong> in combination with the appropriate athletic response. Our training lights are portable and can be arranged in any configuration.</p>
    <h2 class="benefits-title">KEY BENEFITS</h2>
    <div class="benefits">
      <div class="benefit">IMPROVED<br>OVERALL<br>PERFORMANCE</div>
      <div class="benefit">IMPROVED<br>DECISION<br>MAKING</div>
      <div class="benefit">IMPROVED<br>VISUAL<br>RESPONSE</div>
    </div>
  </section>

  <div class="photo" role="img" aria-label="Basketball player in a red kit leaping for a dunk in an arena, with three tripod-mounted reaction lights and their carry case in the foreground"></div>

  <footer class="contact">
    <div class="contact-item" style="left:48px">
      <svg viewBox="0 0 22 24"><polygon points="11,0 22,6 22,18 11,24 0,18 0,6" fill="var(--red-icon)"/><path d="M11 6a4 4 0 0 0-4 4c0 3 4 7 4 7s4-4 4-7a4 4 0 0 0-4-4z" fill="none" stroke="#fff" stroke-width="1.4"/><circle cx="11" cy="10" r="1.4" fill="#fff"/></svg>
      Maple Bend, California
    </div>
    <span class="contact-rule" style="left:295px"></span>
    <div class="contact-item" style="left:351px">
      <svg viewBox="0 0 22 24"><polygon points="11,0 22,6 22,18 11,24 0,18 0,6" fill="var(--red-icon)"/><path d="M7 7l2-1 2 3-1.5 1.2a6 6 0 0 0 3 3L14 11.7l3 2-1 2c-4 .5-9.5-5-9-8.7z" fill="none" stroke="#fff" stroke-width="1.3" stroke-linejoin="round"/></svg>
      Tel: (555) 010-2847
    </div>
    <span class="contact-rule" style="left:570px"></span>
    <div class="contact-item" style="left:624px">
      <svg viewBox="0 0 22 24"><polygon points="11,0 22,6 22,18 11,24 0,18 0,6" fill="var(--red-icon)"/><rect x="5.5" y="8" width="11" height="8" fill="none" stroke="#fff" stroke-width="1.3"/><path d="M5.5 8l5.5 4.5L16.5 8" fill="none" stroke="#fff" stroke-width="1.3"/></svg>
      mail@quikkotza.com
    </div>
  </footer>
</body>
</html>
```